Catalog for our Gold Coins for high value market

We need someone who makes our catalog or book for the gold coins of Switzerland.
Please use the Word Document. The text and the images are below. Feel free to make a nice design. Also make a nice design as a title.
Please use Adobe Indesign or Illustrator to make the content adjustable for us if needed.

You could also add a "star rating" from 1-4 for some of the coins with an image. I will do the rating later. It should be a rating of how precious the coins are without entering a price.
You could also adjust the title design with the coins.

Please make at least the following pages:
Title
Table of content
Title Page for each Ares (Aargau Page 6, Appenzell Page 6, Basel Page 8 and so on)
Pages with the content (Coins including the description)

Target Market(s)

Gold coins collectors. Usually those people are rich men.

Requirements
Must have
• Modern design
Should not have
• Not too many colors used. It should be modern. But have some class.

```html
<!DOCTYPE html>
<html lang="de">
<head>
<meta charset="utf-8">
<title>Goldmünzen der Kantone und Eidgenossenschaft – Katalog</title>
<link href="https://fonts.googleapis.com/css2?family=Montserrat:wght@500;600;700&family=Hind:wght@300;400;500&family=Open+Sans:wght@400&display=swap" rel="stylesheet">
<style>
  :root {
    --backdrop: #d8d8d8;
    --ink-dark: #2a2a2c;
    --paper: #f4f4f4;
    --gold: #e3b52a;
    --gold-soft: #d2b062;
    --coin: #d9ae3c;
    --star: #c9a84c;
    --text: #2b2b2b;
    --text-soft: #4a4a4a;
    --rule: #555;
  }
  * { margin: 0; padding: 0; box-sizing: border-box; }
  html, body { width: 1200px; height: 900px; overflow: hidden; }
  body { background: var(--backdrop); position: relative; font-family: "Hind", sans-serif; color: var(--text); }

  .page { position: absolute; }
  .page--dark { background: var(--ink-dark); }
  .page--light { background: var(--paper); }

  /* Cover */
  .cover { left: 48px; top: 66px; width: 354px; height: 354px; overflow: hidden; }
  .cover__photo { position: absolute; inset: 0;
    background: radial-gradient(circle at 35% 70%, rgba(214,172,70,.35), transparent 32%),
                radial-gradient(circle at 85% 30%, rgba(120,140,110,.25), transparent 25%),
                linear-gradient(135deg, #2e2e30, #222224); }
  .cover__title { position: absolute; left: 42px; top: 44px; font-family: "Montserrat", sans-serif; font-weight: 700; font-size: 18.5px; letter-spacing: 2.2px; color: var(--gold); }
  .cover__subtitle { position: absolute; left: 42px; top: 68px; font-family: "Open Sans", sans-serif; font-size: 8.8px; letter-spacing: .5px; color: var(--gold); }

  /* Contents spread */
  .spread-blank { left: 473px; top: 66px; width: 331px; height: 354px; }
  .contents { left: 804px; top: 66px; width: 330px; height: 354px; }
  .contents__heading { position: absolute; left: 40px; top: 38px; font-family: "Montserrat", sans-serif; font-weight: 700; font-size: 10.5px; letter-spacing: 1.6px; color: var(--text); }
  .toc { position: absolute; left: 88px; top: 62px; width: 158px; list-style: none; }
  .toc__group { border-bottom: 1px solid var(--rule); padding-bottom: 8px; margin-bottom: 8px; }
  .toc__entry { display: flex; justify-content: space-between; font-size: 5.4px; line-height: 9.6px; color: var(--text-soft); font-weight: 300; }
  .toc__entry--section { font-weight: 500; color: var(--text); }
  .page-footer { position: absolute; bottom: 12px; font-size: 4.6px; color: var(--text-soft); letter-spacing: .2px; }
  .page-footer b { font-weight: 500; color: var(--text); }
  .page-footer--right { right: 11px; }
  .page-footer--left { left: 13px; }
  .page--dark .page-footer { color: #bbb; }
  .page--dark .page-footer b { color: #fff; }

  /* Coin spread */
  .coin-page { left: 473px; top: 471px; width: 331px; height: 355px; }
  .coin-page__title { position: absolute; left: 35px; top: 39px; font-family: "Montserrat", sans-serif; font-weight: 700; font-size: 10.2px; letter-spacing: .6px; color: var(--text); }
  .coin-page__lead { position: absolute; left: 35px; top: 59px; width: 256px; font-size: 5.3px; line-height: 8.4px; font-weight: 300; color: var(--text-soft); }
  .coin-photo { position: absolute; display: flex; align-items: center; justify-content: space-around; }
  .coin-photo--band { left: 0; top: 94px; width: 181px; height: 86px; background: var(--ink-dark); padding: 0 14px; }
  .coin-photo--loose { left: 155px; top: 218px; width: 136px; height: 69px; justify-content: space-between; }
  .coin-photo__face { width: 62px; height: 62px; border-radius: 50%; background: radial-gradient(circle at 40% 35%, #eccb5e, var(--coin) 60%, #b88d2a); }
  .coin-photo--loose .coin-photo__face { width: 64px; height: 64px; }
  .coin-caption { position: absolute; text-align: center; font-family: "Montserrat", sans-serif; font-weight: 600; font-size: 5.4px; letter-spacing: .3px; color: var(--text); }
  .coin-caption--first { left: 24px; top: 188px; width: 132px; }
  .coin-caption--second { left: 155px; top: 295px; width: 136px; }
  .rating { position: absolute; display: flex; gap: 1.5px; }
  .rating--first { left: 68px; top: 199px; }
  .rating--second { left: 201px; top: 306px; }
  .rating svg { width: 9px; height: 9px; }

  .canton-title { left: 804px; top: 471px; width: 330px; height: 355px; overflow: hidden; }
  .canton-title__photo { position: absolute; inset: 0;
    background: radial-gradient(circle at 45% 78%, rgba(200,162,70,.35), transparent 30%),
                radial-gradient(circle at 25% 20%, rgba(150,150,150,.25), transparent 30%),
                linear-gradient(160deg, #2c2c2e, #1f1f21); }
  .canton-title__name { position: absolute; left: 174px; top: 176px; font-family: "Montserrat", sans-serif; font-weight: 600; font-size: 17px; letter-spacing: 2.2px; color: var(--gold-soft); }
</style>
</head>
<body>

<section class="page page--dark cover">
  <div class="cover__photo" role="img" aria-label="Fotografie: Schweizer Goldmünzen, Lupe, Sukkulente, Lederetui und Füller auf dunklem Grund"></div>
  <h1 class="cover__title">GOLDMÜNZEN</h1>
  <p class="cover__subtitle">der Kantone und Eidgenossenschaft</p>
</section>

<section class="page page--dark spread-blank"></section>

<section class="page page--light contents">
  <h2 class="contents__heading">INHALT</h2>
  <ul class="toc">
    <li class="toc__group">
      <div class="toc__entry toc__entry--section"><span>AARGAU</span><span>5</span></div>
      <div class="toc__entry"><span>Abt Benedikt von Erlenbach 1688 – 1727</span><span>6</span></div>
    </li>
    <li class="toc__group">
      <div class="toc__entry toc__entry--section"><span>APPENZELL</span><span>7</span></div>
      <div class="toc__entry"><span>Appenzell Innerrhoden</span><span>8</span></div>
    </li>
    <li class="toc__group">
      <div class="toc__entry toc__entry--section"><span>BASEL</span><span>9</span></div>
      <div class="toc__entry"><span>Reichsmünzstätte</span><span>10</span></div>
      <div class="toc__entry"><span>Reichsmünzstätte 15. Jahrhundert</span><span>11</span></div>
      <div class="toc__entry"><span>Stadt Basel 16. Jahrhundert</span><span>13</span></div>
      <div class="toc__entry"><span>Stadt Basel 17. Jahrhundert</span><span>14</span></div>
      <div class="toc__entry"><span>Stadt Basel 18. Jahrhundert</span><span>16</span></div>
      <div class="toc__entry"><span>Bistum Basel</span><span>19</span></div>
      <div class="toc__entry"><span>Johann Franz von Tannegg 1651 -1656</span><span>19</span></div>
      <div class="toc__entry"><span>Johann Konrad I. von Birkenau 1656-1693</span><span>19</span></div>
      <div class="toc__entry"><span>Johann Konrad II. von Falkenstein-Moos 1705-1737</span><span>19</span></div>
    </li>
    <li class="toc__group">
      <div class="toc__entry toc__entry--section"><span>BERN</span><span>20</span></div>
      <div class="toc__entry"><span>Bern – 15. Jahrhundert</span><span>20</span></div>
      <div class="toc__entry"><span>Bern – 16. Jahrhundert</span><span>20</span></div>
      <div class="toc__entry"><span>Bern – 17. Jahrhundert</span><span>22</span></div>
      <div class="toc__entry"><span>Bern – 18. Jahrhundert</span><span>26</span></div>
      <div class="toc__entry"><span>Bern – 19. Jahrhundert</span><span>47</span></div>
    </li>
  </ul>
  <p class="page-footer page-footer--right">INHALT | Page <b>1</b></p>
</section>

<section class="page page--light coin-page">
  <h2 class="coin-page__title">ABT BENEDIKT VON ERLENBACH 1688 – 1727</h2>
  <p class="coin-page__lead">Benedikt Erlenbach (* 2. März 1650 in Lenzwil; † 9. Oktober 1727 auf Schloss Hohenried) war ein Schweizer Benediktinermönch. Von 1688 bis 1705 war er Abt, danach bis zu seinem Tod erster Fürstabt des Klosters Talbach in den Freien Ämtern (im heutigen Kanton Aargau).</p>

  <div class="coin-photo coin-photo--band" role="img" aria-label="Fotografie: 5 Dukaten 1722, Vorder- und Rückseite auf dunklem Grund">
    <span class="coin-photo__face"></span><span class="coin-photo__face"></span>
  </div>
  <p class="coin-caption coin-caption--first">5 DUKATEN (JAHR 1722, KAT 4-21B)</p>
  <div class="rating rating--first" aria-label="3,5 von 4 Sternen">
    <svg viewBox="0 0 24 24"><polygon fill="var(--star)" points="12,1 15,9 23,9 16.5,14 19,22 12,17 5,22 7.5,14 1,9 9,9"/></svg>
    <svg viewBox="0 0 24 24"><polygon fill="var(--star)" points="12,1 15,9 23,9 16.5,14 19,22 12,17 5,22 7.5,14 1,9 9,9"/></svg>
    <svg viewBox="0 0 24 24"><polygon fill="var(--star)" points="12,1 15,9 23,9 16.5,14 19,22 12,17 5,22 7.5,14 1,9 9,9"/></svg>
    <svg viewBox="0 0 24 24"><polygon fill="none" stroke="var(--star)" stroke-width="1.5" points="12,1 15,9 23,9 16.5,14 19,22 12,17 5,22 7.5,14 1,9 9,9"/><polygon fill="var(--star)" points="12,1 12,17 5,22 7.5,14 1,9 9,9"/></svg>
  </div>

  <div class="coin-photo coin-photo--loose" role="img" aria-label="Fotografie: Dukat 1722, Vorder- und Rückseite freigestellt">
    <span class="coin-photo__face"></span><span class="coin-photo__face"></span>
  </div>
  <p class="coin-caption coin-caption--second">DUKAT (JAHR 1722, KAT 4-22B)</p>
  <div class="rating rating--second" aria-label="4 von 4 Sternen">
    <svg viewBox="0 0 24 24"><polygon fill="var(--star)" points="12,1 15,9 23,9 16.5,14 19,22 12,17 5,22 7.5,14 1,9 9,9"/></svg>
    <svg viewBox="0 0 24 24"><polygon fill="var(--star)" points="12,1 15,9 23,9 16.5,14 19,22 12,17 5,22 7.5,14 1,9 9,9"/></svg>
    <svg viewBox="0 0 24 24"><polygon fill="var(--star)" points="12,1 15,9 23,9 16.5,14 19,22 12,17 5,22 7.5,14 1,9 9,9"/></svg>
    <svg viewBox="0 0 24 24"><polygon fill="var(--star)" points="12,1 15,9 23,9 16.5,14 19,22 12,17 5,22 7.5,14 1,9 9,9"/></svg>
  </div>

  <p class="page-footer page-footer--left">Page <b>7</b> | AARGAU</p>
</section>

<section class="page page--dark canton-title">
  <div class="canton-title__photo" role="img" aria-label="Fotografie: Lupe, Zange und drei Appenzeller Goldmünzen auf dunklem Grund"></div>
  <h2 class="canton-title__name">APPENZELL</h2>
  <p class="page-footer page-footer--right">APPENZELL | Page <b>8</b></p>
</section>

</body>
</html>
```